Timid Kitten Clinic Business Card Design

I need a business card designed for my cat only veterinary clinic. I will upload the logo that I would like included on the card. Please include:
Business Name: The Timid Kitten Clinic
Address: 4827 W. 39th Ln, Scottsdale, AZ 85317
Phone #: 480-555-6314
Website URL: www.timidkittenvet.example
And the Doctors Name: Marla Quint, DVM

```html
<!DOCTYPE html>
<html lang="en">
<head>
<meta charset="utf-8">
<title>The Timid Kitten Clinic – Business Card</title>
<link rel="stylesheet" href="https://fonts.googleapis.com/css2?family=Quicksand:wght@500;600&display=swap">
<style>
  :root {
    --backdrop: #3d5068;
    --card-white: #ffffff;
    --band-light: #e2e7f1;
    --band-mid: #c9d4e6;
    --brand-blue: #4f86b8;
    --text-dark: #222428;
    --pattern-bg: #e0e6f0;
    --mark-fill: #2c3344;
  }
  * { margin: 0; padding: 0; box-sizing: border-box; }
  html, body { width: 1200px; height: 1200px; overflow: hidden; }
  body { background: var(--backdrop); position: relative; font-family: "Quicksand", sans-serif; }

  .card {
    position: absolute;
    left: 271px;
    width: 672px;
    height: 399px;
    overflow: hidden;
  }
  .card--front { top: 162px; background: var(--card-white); }
  .card--back  { top: 631px; background: var(--pattern-bg); }

  .card__shapes { position: absolute; inset: 0; width: 672px; height: 399px; }

  .doctor-name {
    position: absolute;
    right: 29px;
    top: 20px;
    font-size: 34px;
    font-weight: 500;
    color: var(--brand-blue);
    letter-spacing: 0.5px;
  }

  .contact {
    position: absolute;
    left: 358px;
    display: flex;
    align-items: center;
    gap: 10px;
    font-size: 19px;
    font-weight: 600;
    color: var(--text-dark);
    line-height: 1.35;
  }
  .contact--address { top: 150px; }
  .contact--phone { top: 226px; }
  .contact__icon { width: 36px; height: 36px; flex: none; }

  .website {
    position: absolute;
    right: 29px;
    top: 347px;
    font-size: 29px;
    font-weight: 500;
    color: var(--card-white);
    letter-spacing: 0.5px;
  }

  .clinic-mark {
    position: absolute;
    left: 36px;
    top: 45px;
    width: 294px;
    height: 294px;
    border-radius: 50%;
    background: var(--mark-fill);
  }
  .clinic-name {
    position: absolute;
    left: 356px;
    top: 166px;
    width: 290px;
    font-family: "Quicksand", sans-serif;
    font-weight: 600;
    font-size: 30px;
    line-height: 1.25;
    color: var(--text-dark);
  }
</style>
</head>
<body>

<section class="card card--front" aria-label="Business card front">
  <svg class="card__shapes" viewBox="0 0 672 399" aria-hidden="true">
    <defs>
      <linearGradient id="photo-fade" x1="0" y1="0" x2="1" y2="0">
        <stop offset="0" stop-color="#9c948e"/>
        <stop offset="0.55" stop-color="#c8c2bf"/>
        <stop offset="1" stop-color="#ffffff" stop-opacity="0"/>
      </linearGradient>
    </defs>
    <path d="M0 0 H672 V118 C560 108 470 60 330 46 C200 34 90 60 0 40 Z" fill="var(--band-light)"/>
    <path d="M0 330 C150 300 300 318 420 296 C520 278 610 270 672 262 V399 H0 Z" fill="var(--band-mid)"/>
    <path d="M0 340 C140 318 260 330 380 320 C500 306 600 300 672 300 V399 H0 Z" fill="var(--brand-blue)"/>
  </svg>
  <svg class="card__shapes" viewBox="0 0 672 399" role="img" aria-label="Photo of a grey and white cat resting on a soft blanket">
    <path d="M0 80 C90 96 200 70 342 90 V320 C240 330 120 318 0 334 Z" fill="url(#photo-fade)"/>
  </svg>

  <p class="doctor-name">Marla Quint, DVM</p>

  <div class="contact contact--address">
    <svg class="contact__icon" viewBox="0 0 36 36" aria-hidden="true">
      <circle cx="18" cy="18" r="16.5" fill="none" stroke="var(--brand-blue)" stroke-width="1.5"/>
      <path d="M18 9 a6 6 0 0 1 6 6 c0 4.5 -6 11 -6 11 s-6 -6.5 -6 -11 a6 6 0 0 1 6 -6 z" fill="var(--brand-blue)"/>
      <circle cx="18" cy="15" r="2.2" fill="var(--card-white)"/>
    </svg>
    <p>4827 W. 39th Ln,<br>Scottsdale, AZ 85317</p>
  </div>

  <div class="contact contact--phone">
    <svg class="contact__icon" viewBox="0 0 36 36" aria-hidden="true">
      <circle cx="18" cy="18" r="16.5" fill="none" stroke="var(--brand-blue)" stroke-width="1.5"/>
      <path d="M12.5 10.5 l3 -0.5 1.6 4 -2 1.5 c0.9 2 2.4 3.5 4.4 4.4 l1.5 -2 4 1.6 -0.5 3 c-0.3 1 -1.2 1.5 -2.2 1.4 C16.5 23.3 12.7 19.5 12.1 13.7 c-0.1 -1 0.4 -2.9 0.4 -3.2 z" fill="var(--brand-blue)"/>
      <path d="M20 10.5 a5.5 5.5 0 0 1 5.5 5.5 M20 13.3 a2.7 2.7 0 0 1 2.7 2.7" fill="none" stroke="var(--brand-blue)" stroke-width="1.3" stroke-linecap="round"/>
    </svg>
    <p>480-555-6314</p>
  </div>

  <p class="website">www.timidkittenvet.example</p>
</section>

<section class="card card--back" aria-label="Business card back">
  <div class="clinic-mark" aria-hidden="true"></div>
  <p class="clinic-name">The Timid Kitten Clinic</p>
</section>

</body>
</html>
```